Law Firm Letterhead

We are looking for a letterhead for our military/veterans law firm. We like simplicity and clean, modern, flat, uncluttered designs. Our logo font is DIN 1451, and our website/business card info font is Helvetica Neue.

Required Information:

- Logo/Graphic: Please see attached logo / business card for ideas. Please also review firm website.

- Motto: A law firm for service members and veterans

- Web Address: www.harborlinecounsel.com

- Email: info@harborlinecounsel.com

- Phone: 866-402-1953

Colors: We prefer either a blue/grey or an all-blue color scheme. The blue in our logo is #336699.

Please DO NOT submit more than 3 designs. Spamming designs with only minor changes between the designs is not appreciated. We can evaluate your quality and direction by your best 1 or 2 designs.

Thank you!

```html
<!DOCTYPE html>
<html lang="en">
<head>
<meta charset="utf-8">
<title>Harborline Counsel Letterhead</title>
<link rel="stylesheet" href="https://fonts.googleapis.com/css2?family=Barlow+Condensed:wght@600&family=Barlow:wght@400;500&display=swap">
<style>
  :root {
    --brand-blue: #336699;
    --ink: #2b2b2b;
    --paper: #ffffff;
    --backdrop: #e9e9e9;
  }
  html, body {
    margin: 0;
    padding: 0;
    width: 943px;
    height: 1200px;
    overflow: hidden;
    background: var(--backdrop);
  }
  .letterhead {
    position: absolute;
    left: 69px;
    top: 100px;
    width: 805px;
    height: 1040px;
    background: var(--paper);
    box-shadow: 0 1px 4px rgba(0,0,0,0.12);
  }
  .firm-name {
    position: absolute;
    right: 33px;
    top: 16px;
    display: flex;
    align-items: center;
    gap: 10px;
    margin: 0;
    font-family: "Barlow Condensed", "Arial Narrow", sans-serif;
    font-weight: 600;
    font-size: 40px;
    line-height: 1;
    color: var(--brand-blue);
    letter-spacing: 0.5px;
  }
  .firm-name .mark {
    width: 14px;
    height: 14px;
    background: var(--brand-blue);
  }
  .contact {
    position: absolute;
    right: 33px;
    top: 102px;
    margin: 0;
    font-family: "Barlow", "Helvetica Neue", Arial, sans-serif;
    font-size: 14.5px;
    line-height: 22px;
    color: var(--ink);
    text-align: right;
  }
  .contact .label { color: var(--brand-blue); }
  .footer {
    position: absolute;
    left: 0;
    right: 0;
    bottom: 14px;
    text-align: center;
    font-family: "Barlow", "Helvetica Neue", Arial, sans-serif;
    color: var(--ink);
  }
  .motto {
    margin: 0;
    font-size: 16px;
    font-weight: 500;
    letter-spacing: 1.4px;
    line-height: 22px;
  }
  .website {
    margin: 0;
    font-size: 14px;
    line-height: 22px;
  }
</style>
</head>
<body>
  <main class="letterhead">
    <h1 class="firm-name"><span class="mark"></span>HARBORLINE COUNSEL</h1>
    <p class="contact">
      <span class="label">p:</span> 866-402-1953<br>
      <span class="label">e:</span> info@harborlinecounsel.com
    </p>
    <footer class="footer">
      <p class="motto">A law firm for service members and veterans</p>
      <p class="website">www.harborlinecounsel.com</p>
    </footer>
  </main>
</body>
</html>
```